Acoustic Album Needs Cover Design

Bela Moravecz - Reflections: Quiet Harbor

The cover has five parts, each one has obligatory features:

The design in general could be that the person on the pictures is in white, empty space. Solve the shadows as you like, or use no shadows. Up to you.
The album is a happy, minimalistic, zen-like, acoustic album.

I. Main cover

Title: Reflections: Quiet Harbor
Artist: Bela Moravecz
Image “01 main cover”

II. Cover inside

Track list (12 songs) with durations
All songs written by Bela Moravecz
Copyright Velunotes 2016.
Image “02 cover inside”

III. Disc

Artist: Bela Moravecz
All songs written by Bela Moravecz (round on the edge)
Copyright Velunotes 2016. (round on the edge)
www.velunotes.example (round on the edge)

IV. Under the disc

No words, only some design feature. (Not one of the three images!)

V. Cover back

Track list (same as cover inside)
Copyright Velunotes 2016.
www.velunotes.example
Image “05 backside”
The paper of this page is longer than the main cover, because it is to be turned up when put in the CD case, and there is the spine with the name of the Artist and Title of the album. On both ends.

Important:
The main cover I need in RGB and also CMYK, all the others only CMYK.
I need the work file (cdr, ai or whatever you use)
I need the CMYK images prepared for printing (sizes set, and that little extra on the edges).
I need the RGB main cover cover in jpeg, 3000x3000 pixels.
That's all. :)

The most important of these all is of course the main cover RGB. Make this one first!

Here’s a sample to listen, it might inspire you:
https://files.sharebinex.example/u/48302716/Quiet%20Harbor%20medley%2020160118.mp3

If you take a closer look at my website, you can see the whole concept.

Good luck and enjoy!
Regards,
Bela

Target Market(s)

New Age spiritual people.

Requirements
Must have
• The three images:
• https://www.sharebinex.example/s/kq7rmzwpt3hbyfa/01%20main%20cover%2020160221.jpg?dl=0
• https://www.sharebinex.example/s/9pluvnexd4q2mrt/02%20cover%20inside%2020160221.jpg?dl=0
• https://www.sharebinex.example/s/tjb3oyhcw8kfz1d/05%20backside%2020160221.jpg?dl=0
• If there's a technical problem, let me know!

```html
<!DOCTYPE html>
<html lang="en">
<head>
<meta charset="utf-8">
<title>Bela Moravecz – Reflections: Quiet Harbor – Back Insert</title>
<link rel="stylesheet" href="https://fonts.googleapis.com/css2?family=Saira+Condensed:wght@200;300&display=swap">
<style>
  :root {
    --page-bg: #e4ddc6;
    --insert-top: #f6f6f7;
    --insert-bottom: #cfd2d8;
    --photo-light: #eef0f4;
    --photo-shirt: #a9c3e8;
    --photo-trousers: #c7b79a;
    --track-grey: #8b8b8e;
    --credit-blue: #6f89b9;
  }
  * { margin: 0; padding: 0; box-sizing: border-box; }
  html, body {
    width: 1200px; height: 1200px; overflow: hidden;
    background: var(--page-bg);
  }
  .back-insert {
    position: absolute;
    left: 40px; top: 118px;
    width: 1120px; height: 965px;
    background: linear-gradient(160deg, var(--insert-top) 0%, #e9eaed 55%, var(--insert-bottom) 100%);
    font-family: "Saira Condensed", "Arial Narrow", sans-serif;
  }
  .artist-photo {
    position: absolute;
    left: 60px; top: 86px;
    width: 320px; height: 820px;
    background:
      linear-gradient(180deg,
        var(--photo-light) 0%,
        var(--photo-light) 14%,
        var(--photo-shirt) 16%,
        var(--photo-shirt) 46%,
        var(--photo-trousers) 48%,
        var(--photo-trousers) 94%,
        var(--photo-light) 100%);
    opacity: 0.55;
    border-radius: 4px;
  }
  .track-list {
    position: absolute;
    left: 520px; top: 84px;
    width: 520px;
    list-style: none;
    color: var(--track-grey);
    font-weight: 200;
    font-size: 36px;
    line-height: 48px;
  }
  .track {
    display: flex;
    justify-content: flex-end;
  }
  .track-title { text-align: right; }
  .track-number {
    width: 61px;
    margin-left: 0;
    padding-left: 0;
    text-align: left;
    position: relative;
    left: 61px;
  }
  .track-list { transform: translateX(-61px); }
  .credits {
    position: absolute;
    right: 55px; top: 858px;
    text-align: right;
    color: var(--credit-blue);
    font-weight: 300;
    font-size: 30px;
    line-height: 35px;
  }
</style>
</head>
<body>
  <section class="back-insert">
    <div class="artist-photo" role="img" aria-label="Full-length photo of the artist standing barefoot in a light blue shirt and beige trousers, holding an acoustic guitar"></div>

    <ol class="track-list">
      <li class="track"><span class="track-title">TRACK SOMETHING ONE</span><span class="track-number">01</span></li>
      <li class="track"><span class="track-title">TRACK SOMETHING TO</span><span class="track-number">02</span></li>
      <li class="track"><span class="track-title">TRACK SOMETHING THREE</span><span class="track-number">03</span></li>
      <li class="track"><span class="track-title">TRACK SOMETHING FOUR</span><span class="track-number">04</span></li>
      <li class="track"><span class="track-title">TRACK SOMETHING FIVE</span><span class="track-number">05</span></li>
      <li class="track"><span class="track-title">TRACK SOMETHING SIX</span><span class="track-number">06</span></li>
      <li class="track"><span class="track-title">TRACK SOMETHING SEVEN</span><span class="track-number">07</span></li>
      <li class="track"><span class="track-title">TRACK SOMETHING EIGHT</span><span class="track-number">08</span></li>
      <li class="track"><span class="track-title">TRACK SOMETHING NINE</span><span class="track-number">09</span></li>
      <li class="track"><span class="track-title">TRACK SOMETHING TEN</span><span class="track-number">10</span></li>
      <li class="track"><span class="track-title">TRACK SOMETHING ELEVEN</span><span class="track-number">11</span></li>
      <li class="track"><span class="track-title">TRACK SOMETHING TWELVE</span><span class="track-number">12</span></li>
    </ol>

    <p class="credits">ALL SONGS WRITTEN BY BELA MORAVECZ<br>COPYRIGHT VELUNOTES 2016.</p>
  </section>
</body>
</html>
```